Storm Restoration Contractor needs a professional business card design

Looking for a professional business card design. Not looking for your cheapo MS Word standard ones that are readily available. Dont want it to be cookie cutter look like ones readily available online. We just recently changed our logo and want to freshen up all our documents. Our company handles restoring a property back to a pre-loss condition after a storm damages it. For example, wind, hail, flood, fire losses.

Target Market(s)

Property Owners, Homeowners, Property Owners, Commercial Property Owners, Property Management Companies, Hail and Wind Damaged Properties

Industry/Entity Type

Construction Company

Contact Information for Business Card

Bramwell Outworks
555-418-7302
555-418-9047 fax
www.bramwelloutworks.example
info@bramwelloutworks.example

Requirements
Must have
• Clean, Professional, fresh look
• Storm Restoration, Roofing, Siding, Windows
Nice to have
• If there is a way to incorporate storms that may be cool.

```html
<!DOCTYPE html>
<html lang="en">
<head>
<meta charset="utf-8">
<title>Bramwell Outworks – Business Card</title>
<link rel="stylesheet" href="https://fonts.googleapis.com/css2?family=Open+Sans:wght@400;600;700&display=swap">
<style>
  :root {
    --stage: #e9e7e4;
    --card-white: #ffffff;
    --slate: #58595b;
    --brand-blue: #1e73be;
    --ink: #4a4a4c;
    --rule: #c9c9cb;
  }
  * { box-sizing: border-box; margin: 0; padding: 0; }
  html, body { width: 1200px; height: 675px; overflow: hidden; }
  body {
    background: var(--stage);
    font-family: "Open Sans", Arial, sans-serif;
    display: flex;
    align-items: center;
    justify-content: center;
    gap: 40px;
  }
  .card {
    position: relative;
    width: 540px;
    height: 309px;
    overflow: hidden;
    box-shadow: 0 6px 18px rgba(0,0,0,0.18);
  }

  /* Back side */
  .card-back {
    background: var(--slate);
    color: #fff;
    display: flex;
    flex-direction: column;
    align-items: center;
    justify-content: center;
    text-align: center;
  }
  .brand {
    display: flex;
    align-items: center;
    gap: 10px;
    font-weight: 700;
    font-size: 22px;
    letter-spacing: 0.5px;
    color: var(--brand-blue);
    white-space: nowrap;
  }
  .brand-dot {
    width: 22px; height: 22px;
    border-radius: 50%;
    background: var(--brand-blue);
    flex: none;
  }
  .card-back .brand { color: #fff; margin-bottom: 22px; }
  .services { font-size: 14px; margin-bottom: 4px; }
  .back-url { font-size: 14px; color: #4a9be0; }

  /* Front side */
  .card-front { background: var(--card-white); }
  .front-brand {
    position: absolute;
    left: 32px; top: 112px;
    font-size: 18px;
    gap: 8px;
  }
  .front-brand .brand-dot { width: 20px; height: 20px; }
  .divider {
    position: absolute;
    left: 254px; top: 62px;
    width: 1px; height: 140px;
    background: var(--rule);
  }
  .holder { position: absolute; left: 272px; right: 18px; top: 60px; }
  .holder-name { font-size: 21px; font-weight: 700; color: var(--brand-blue); line-height: 1.2; }
  .holder-role { font-size: 13px; color: var(--ink); margin-bottom: 14px; }
  .contacts { list-style: none; }
  .contacts li {
    display: flex; align-items: center; gap: 8px;
    font-size: 13px; color: var(--ink); line-height: 19px;
    white-space: nowrap;
  }
  .contacts svg { width: 13px; height: 13px; flex: none; }
  .contacts .url-domain { color: var(--brand-blue); }
  .band-left {
    position: absolute; left: 0; bottom: 0;
    width: 228px; height: 48px;
    background: var(--brand-blue);
  }
  .band-right-slate {
    position: absolute; left: 240px; right: 0; bottom: 12px;
    height: 20px; background: var(--slate);
  }
  .band-right-blue {
    position: absolute; left: 240px; right: 0; bottom: 0;
    height: 12px; background: var(--brand-blue);
  }
</style>
</head>
<body>

  <section class="card card-back" aria-label="Card back">
    <div class="brand"><span class="brand-dot"></span>Bramwell Outworks</div>
    <p class="services">Storm Restoration | Roofing | Siding | Windows</p>
    <p class="back-url">www.bramwelloutworks.example</p>
  </section>

  <section class="card card-front" aria-label="Card front">
    <div class="brand front-brand"><span class="brand-dot"></span>Bramwell Outworks</div>
    <div class="divider"></div>
    <div class="holder">
      <p class="holder-name">Dorian Kell</p>
      <p class="holder-role">Director</p>
      <ul class="contacts">
        <li>
          <svg viewBox="0 0 16 16" aria-hidden="true"><circle cx="8" cy="8" r="8" fill="#1e73be"/><path d="M5.2 4.2l1.4-.4 1 2-1 .8a5 5 0 0 0 1.9 1.9l.8-1 2 1-.4 1.4c-3 .3-6-2.7-5.7-5.7z" fill="#fff"/></svg>
          555-418-7302
        </li>
        <li>
          <svg viewBox="0 0 16 16" aria-hidden="true"><circle cx="8" cy="8" r="8" fill="#1e73be"/><rect x="5.5" y="3.5" width="5" height="3" fill="#fff"/><rect x="4" y="6.5" width="8" height="4" rx="1" fill="#fff"/><rect x="5.5" y="9.5" width="5" height="3" fill="#fff" stroke="#1e73be" stroke-width=".6"/></svg>
          555-418-9047
        </li>
        <li>
          <svg viewBox="0 0 16 16" aria-hidden="true"><circle cx="8" cy="8" r="8" fill="#1e73be"/><rect x="4" y="5" width="8" height="6" fill="#fff"/><path d="M4 5l4 3.2L12 5" fill="none" stroke="#1e73be" stroke-width=".9"/></svg>
          info@bramwelloutworks.example
        </li>
        <li>
          <svg viewBox="0 0 16 16" aria-hidden="true"><circle cx="8" cy="8" r="8" fill="#1e73be"/><g fill="none" stroke="#fff" stroke-width=".9"><circle cx="8" cy="8" r="4"/><ellipse cx="8" cy="8" rx="1.8" ry="4"/><path d="M4 8h8"/></g></svg>
          <span>www.<span class="url-domain">bramwelloutworks</span>.example</span>
        </li>
      </ul>
    </div>
    <div class="band-left"></div>
    <div class="band-right-slate"></div>
    <div class="band-right-blue"></div>
  </section>

</body>
</html>
```